Flyer design for carpet cleaning

We want to design a flyer for our new wing of business. Carpet and upholstery cleaning. We want it to match with the previous branding so please refer out website. Www.brivelcora.co.uk and see the carpet section. We currently have 4 services
Carpet and rug (cleaning and stain protection coating)
Upholstery and curtain (cleaning and stain protection coating)
Floor and patio (cleaning and polishing)
Antimicrobial (90 days self disinfecting coating)
Our price list is on the website I will attach some qr codes that I would like to put on the website.
Please use these terms
- quickest dry time
-24 hours call out
-based in London
-100% satisfaction guaranteed
-Low moisture cleaning
-Nano technology based stain protectant
- long lasting antimicrobial protection
Adding photos or not adding is designer choice and even putting price list or not is designer choice. The prices can be starting from format or full price list at the back page and other details in front

```html
<!DOCTYPE html>
<html lang="en">
<head>
<meta charset="utf-8">
<title>Brivelcora – Carpet and Upholstery Cleaning Flyer</title>
<link rel="stylesheet" href="https://fonts.googleapis.com/css2?family=Poppins:wght@400;500;600;700;800&display=swap">
<style>
  :root{
    --navy:#0b1f4d;
    --blue:#1565d8;
    --sky:#4fb3ff;
    --ink:#1c2433;
    --muted:#5b6678;
    --paper:#ffffff;
    --stage:#e7e8ea;
    --photo-a:#c9d6e6;
    --photo-b:#7f97b8;
  }
  *{box-sizing:border-box;margin:0;padding:0}
  html,body{width:1200px;height:2364px;overflow:hidden}
  body{background:var(--stage);font-family:"Poppins",Arial,sans-serif;color:var(--ink);position:relative}

  .flyer{position:absolute;left:100px;top:475px;width:1000px;height:1414px;background:var(--paper);overflow:hidden;box-shadow:0 10px 30px rgba(0,0,0,.12)}

  .brand{position:absolute;left:50px;top:48px;display:flex;align-items:center;gap:16px}
  .brand-mark{width:58px;height:58px;border-radius:50%;background:var(--blue)}
  .brand-name{font-size:40px;font-weight:700;color:var(--blue);line-height:1}
  .brand-tag{font-size:14px;color:var(--muted);margin-top:6px}

  .hero-photo{position:absolute;left:430px;top:40px;width:540px;height:500px;border:16px solid var(--blue);border-top-right-radius:40px;border-bottom-left-radius:160px;background:linear-gradient(135deg,var(--photo-a),var(--photo-b));overflow:hidden}
  .hero-inset{position:absolute;left:500px;top:350px;width:170px;height:170px;border-radius:50%;border:10px solid var(--paper);background:linear-gradient(135deg,#d9d4cc,#8f8a82);box-shadow:0 6px 16px rgba(0,0,0,.25)}

  .title-band{position:absolute;left:0;top:262px;width:640px;height:230px;background:var(--navy);clip-path:polygon(0 0,100% 0,88% 100%,0 100%);padding:38px 0 0 50px}
  .title-accent{position:absolute;left:0;top:492px;width:560px;height:14px;background:var(--blue);clip-path:polygon(0 0,100% 0,98% 100%,0 100%)}
  .title{font-size:54px;font-weight:800;line-height:1.08;color:#fff;text-transform:uppercase}
  .title em{font-style:normal;color:var(--sky)}

  .services-head{position:absolute;left:50px;top:570px;font-size:38px;font-weight:500;color:var(--navy)}
  .services-head b{font-weight:800;color:var(--blue)}
  .services-rule{position:absolute;left:50px;top:628px;width:900px;height:3px;background:var(--navy)}

  .services{position:absolute;left:50px;top:665px;width:900px;display:grid;grid-template-columns:1fr 1fr;column-gap:50px;row-gap:36px}
  .service{display:flex;gap:22px;align-items:flex-start}
  .service-photo{flex:0 0 190px;height:130px;border-radius:6px;background:linear-gradient(135deg,var(--photo-a),var(--photo-b))}
  .service-name{font-size:26px;font-weight:700;color:var(--blue);line-height:1.15;margin-top:6px}
  .service-note{font-size:18px;color:var(--ink);margin-top:6px;line-height:1.3}

  .features{position:absolute;left:30px;top:1040px;width:940px;display:flex;justify-content:space-between}
  .feature{width:124px;text-align:center}
  .feature-icon{width:76px;height:76px;border-radius:50%;background:var(--blue);margin:0 auto 12px;display:flex;align-items:center;justify-content:center;box-shadow:0 0 0 5px #d6e6fb}
  .feature-label{font-size:15px;line-height:1.3;color:var(--ink);font-weight:500}

  .footer-line{position:absolute;left:0;top:1290px;width:1000px;height:6px;background:var(--blue)}
  .footer{position:absolute;left:0;top:1296px;width:1000px;height:118px;display:flex}
  .footer-phone{width:340px;display:flex;align-items:center;gap:14px;padding-left:50px;font-size:28px;font-weight:700;color:var(--navy)}
  .footer-phone-icon{width:46px;height:46px;border-radius:50%;background:var(--blue);display:flex;align-items:center;justify-content:center}
  .footer-info{flex:1;background:var(--navy);clip-path:polygon(6% 0,100% 0,100% 100%,0 100%);display:flex;align-items:center;justify-content:space-between;padding:0 50px 0 90px;color:#fff;font-size:18px;line-height:1.35}
  .footer-web{color:var(--sky);font-weight:600}
</style>
</head>
<body>
<main class="flyer">
  <div class="brand">
    <div class="brand-mark"></div>
    <div>
      <div class="brand-name">Brivelcora</div>
      <div class="brand-tag">Advanced cleaning and coating</div>
    </div>
  </div>

  <div class="hero-photo" role="img" aria-label="Cleaner in blue overalls vacuuming carpet in a bright room"></div>
  <div class="hero-inset" role="img" aria-label="Close-up of a carpet cleaning nozzle on carpet"></div>

  <div class="title-band">
    <h1 class="title">Carpet and<br>upholstery<br><em>cleaning</em></h1>
  </div>
  <div class="title-accent"></div>

  <h2 class="services-head">OUR <b>SERVICES</b></h2>
  <div class="services-rule"></div>

  <section class="services">
    <div class="service">
      <div class="service-photo" role="img" aria-label="Carpet being cleaned with a machine"></div>
      <div><div class="service-name">Carpet and rug</div><div class="service-note">(cleaning and stain protection coating)</div></div>
    </div>
    <div class="service">
      <div class="service-photo" role="img" aria-label="Polished floor and patio tiles"></div>
      <div><div class="service-name">Floor and patio</div><div class="service-note">(cleaning and polishing)</div></div>
    </div>
    <div class="service">
      <div class="service-photo" role="img" aria-label="Sofa upholstery being cleaned"></div>
      <div><div class="service-name">Upholstery and curtain</div><div class="service-note">(cleaning and stain protection coating)</div></div>
    </div>
    <div class="service">
      <div class="service-photo" role="img" aria-label="Blue microscopic antimicrobial surface"></div>
      <div><div class="service-name">Antimicrobial</div><div class="service-note">(90 days self disinfecting coating)</div></div>
    </div>
  </section>

  <section class="features">
    <div class="feature">
      <div class="feature-icon"><svg width="40" height="40" viewBox="0 0 40 40" fill="none" stroke="#fff" stroke-width="3"><circle cx="20" cy="20" r="15"/><path d="M20 11v10l7 4"/></svg></div>
      <div class="feature-label">quickest dry time</div>
    </div>
    <div class="feature">
      <div class="feature-icon"><svg width="40" height="40" viewBox="0 0 24 24" fill="#fff"><path d="M6.6 10.8a15.1 15.1 0 0 0 6.6 6.6l2.2-2.2a1 1 0 0 1 1-.25 11.4 11.4 0 0 0 3.6.57 1 1 0 0 1 1 1V20a1 1 0 0 1-1 1A17 17 0 0 1 3 4a1 1 0 0 1 1-1h3.5a1 1 0 0 1 1 1c0 1.25.2 2.45.57 3.6a1 1 0 0 1-.25 1z"/></svg></div>
      <div class="feature-label">24 hours call out</div>
    </div>
    <div class="feature">
      <div class="feature-icon"><svg width="40" height="40" viewBox="0 0 24 24" fill="#fff"><path d="M12 2a7 7 0 0 0-7 7c0 5.2 7 13 7 13s7-7.8 7-13a7 7 0 0 0-7-7zm0 9.5A2.5 2.5 0 1 1 12 6.5a2.5 2.5 0 0 1 0 5z"/></svg></div>
      <div class="feature-label">based in London</div>
    </div>
    <div class="feature">
      <div class="feature-icon"><svg width="40" height="40" viewBox="0 0 40 40" fill="none" stroke="#fff" stroke-width="4" stroke-linecap="round" stroke-linejoin="round"><path d="M10 21l7 7 13-15"/></svg></div>
      <div class="feature-label">100% satisfaction guaranteed</div>
    </div>
    <div class="feature">
      <div class="feature-icon"><svg width="40" height="40" viewBox="0 0 24 24" fill="#fff"><path d="M12 3s-6 7-6 11a6 6 0 0 0 12 0c0-4-6-11-6-11z"/></svg></div>
      <div class="feature-label">Low moisture cleaning</div>
    </div>
    <div class="feature">
      <div class="feature-icon"><svg width="40" height="40" viewBox="0 0 24 24" fill="none" stroke="#fff" stroke-width="2"><circle cx="12" cy="12" r="3"/><circle cx="12" cy="12" r="8"/><circle cx="12" cy="4" r="1.5" fill="#fff"/><circle cx="19" cy="15" r="1.5" fill="#fff"/><circle cx="5" cy="15" r="1.5" fill="#fff"/></svg></div>
      <div class="feature-label">Nano technology based stain protectant</div>
    </div>
    <div class="feature">
      <div class="feature-icon"><svg width="40" height="40" viewBox="0 0 24 24" fill="none" stroke="#fff" stroke-width="2" stroke-linejoin="round"><path d="M12 2l8 3v6c0 5-3.5 9-8 11-4.5-2-8-6-8-11V5z"/><path d="M8.5 12l2.5 2.5 4.5-5" stroke-linecap="round"/></svg></div>
      <div class="feature-label">long lasting antimicrobial protection</div>
    </div>
  </section>

  <div class="footer-line"></div>
  <footer class="footer">
    <div class="footer-phone">
      <span class="footer-phone-icon"><svg width="24" height="24" viewBox="0 0 24 24" fill="#fff"><path d="M6.6 10.8a15.1 15.1 0 0 0 6.6 6.6l2.2-2.2a1 1 0 0 1 1-.25 11.4 11.4 0 0 0 3.6.57 1 1 0 0 1 1 1V20a1 1 0 0 1-1 1A17 17 0 0 1 3 4a1 1 0 0 1 1-1h3.5a1 1 0 0 1 1 1c0 1.25.2 2.45.57 3.6a1 1 0 0 1-.25 1z"/></svg></span>
      020 7946 0321
    </div>
    <div class="footer-info">
      <div>Brivelcora Ashford Place<br>London W2 5QX</div>
      <div class="footer-web">www.brivelcora.co.uk</div>
    </div>
  </footer>
</main>
</body>
</html>
```